Application Dashboard Skin - Non coded theme only

We are looking for a website color theme/look feel for a new .net dashboard application we are building. Target audience who will be using this are E and C level professionals. We are looking for the following:

Images of optional color themes for our existing dashboard. You can access a temporary version with no styling here: http://vantorquel.net:99/ . Application built in telerik and highcharts.

We are not looking for finished code or application skins. Our development team will take your final design (with specific colors/images/etc. provided) and apply it to the final beta version of the application.

Design considerations:
We are open to creative ideas, but please know that preference will be given to professional designs with emphasis on a consistent brand look/feel. Designs and colors should be focused on quickly identifying and processing the data.

Multiple submissions welcome.

-Pellowrin team

Target Market(s)

IT / Insurance

Industry/Entity Type

Building

Number of Pages Required

3 page

Requirements
Must have
• Application Dashboard link for design: http://vantorquel.net:99/

```html
<!DOCTYPE html>
<html lang="en">
<head>
<meta charset="utf-8">
<title>Ledgerline – Accuracy Results</title>
<link href="https://fonts.googleapis.com/css2?family=Titillium+Web:wght@400;600;700&family=Open+Sans:wght@400;600;700&display=swap" rel="stylesheet">
<style>
:root{
  --navy:#0f3a4e;
  --navy-deep:#0c3142;
  --teal:#174d63;
  --teal-mid:#1b546b;
  --orange:#f7931e;
  --orange-lt:#f9ad2a;
  --red:#d8353c;
  --ink:#1d4f66;
  --text:#333;
  --muted:#7a8790;
  --grey:#e9eaeb;
  --grey-row:#ebebeb;
  --tag:#8a9399;
  --white:#fff;
}
*{box-sizing:border-box;margin:0;padding:0}
html,body{width:1200px;height:875px;overflow:hidden;background:var(--grey)}
body{font-family:"Open Sans",sans-serif;color:var(--text)}
.stage{width:1349px;height:984px;transform:scale(.8895);transform-origin:0 0;position:relative;background:#e6e8e9}
.abs{position:absolute}

/* sidebar */
.sidebar{left:0;top:0;width:391px;height:984px;background:var(--teal)}
.brand{left:0;top:0;width:391px;height:80px;background:var(--white);display:flex;flex-direction:column;justify-content:center;padding-left:42px}
.brand-name{display:flex;align-items:center;gap:8px;font-family:"Titillium Web",sans-serif;font-weight:600;font-size:34px;color:#2a2a2a;line-height:1}
.brand-dot{width:26px;height:26px;border-radius:50%;background:var(--orange)}
.brand-tag{font-size:12px;color:#333;margin-left:190px;margin-top:2px}
.kpi-head{left:0;top:80px;width:391px;height:60px;background:var(--navy);display:flex;align-items:center;padding:0 16px;color:var(--white)}
.kpi-head .tick{width:24px;height:24px;border:2px solid var(--orange);border-radius:50%;margin-right:9px;display:flex;align-items:center;justify-content:center}
.kpi-head h2{font-family:"Titillium Web",sans-serif;font-size:17px;font-weight:700}
.kpi-head .overall{margin-left:auto;font-size:13px;color:#5fc0cf}
.kpi-head .overall b{color:var(--orange)}
.kpi-head .caret{margin-left:14px;width:0;height:0;border-left:6px solid transparent;border-right:6px solid transparent;border-top:7px solid #5fc0cf}
.kpi-list{left:0;top:140px;width:391px;height:500px;background:var(--teal-mid);list-style:none;padding:15px 24px 0 16px}
.kpi-list li{display:flex;align-items:baseline;height:40px;font-size:13px;color:#c7d6dc}
.kpi-list li::before{content:"";width:4px;height:4px;border-radius:50%;background:#c7d6dc;margin-right:7px;transform:translateY(-3px)}
.kpi-list .lead{flex:1;border-bottom:1px dotted #7c9aa6;margin:0 4px;transform:translateY(-3px)}
.kpi-list b{color:var(--white);font-size:13px;width:93px}
.scroll-thumb{left:382px;top:222px;width:3px;height:40px;background:#3e6e80;border-radius:2px}
.ratios{left:0;top:640px;width:391px;height:344px;background:linear-gradient(180deg,var(--navy) 0%,#123f53 60%,var(--navy-deep) 100%)}
.ring-label{font-size:13px;color:var(--white);text-align:center;line-height:20px}
.stat{font-family:"Titillium Web",sans-serif}
.stat small{display:block;font-size:14px;font-weight:700;color:var(--orange);line-height:14px}
.stat span{font-size:30px;color:#dbe4e8;line-height:34px}
.stat-divider{width:1px;background:#315e70}

/* top nav */
.topnav{left:391px;top:0;width:958px;height:80px;background:var(--ink);display:flex}
.tab{height:80px;display:flex;align-items:center;justify-content:center;font-size:14px;color:#9bb8c4;border-right:1px solid #134256}
.tab.active{color:var(--white);font-weight:600;box-shadow:inset 0 -7px 0 var(--orange)}
.user{left:1098px;top:22px;display:flex;align-items:center;height:36px}
.avatar{width:36px;height:36px;background:linear-gradient(160deg,#c98a5a,#6e3c25)}
.hi{font-size:13px;color:#3fa2bd;margin-left:9px}

/* panels */
.panel{background:var(--white)}
.panel-title{font-family:"Titillium Web",sans-serif;font-size:17px;font-weight:600;color:var(--ink)}
.hint{font-size:13px;font-style:italic;color:#777}
.select{background:#eceeef;color:#9aa4a9;font-size:13px;display:flex;align-items:center;padding:0 14px;justify-content:space-between}
.menu i{display:block;width:18px;height:3px;background:#3b5563;margin-bottom:4px}
.regions{font-size:13px;color:#666}

.impact-bar{left:400px;top:457px;width:934px;height:62px;background:var(--ink);display:flex;align-items:center;padding-left:16px;color:var(--white)}
.impact-bar h3{font-family:"Titillium Web",sans-serif;font-weight:600;font-size:17px;margin-left:12px}
.impact-select{left:1156px;top:472px;width:166px;height:32px;background:#14485d;color:#3f89a3;font-size:13px;display:flex;align-items:center;justify-content:space-between;padding:0 14px}
.err-tabs{left:400px;top:519px;height:46px;display:flex}
.err-tab{height:46px;display:flex;align-items:center;justify-content:center;font-size:14px;font-weight:600;color:var(--white);background:#7f8a90;border-right:1px solid #6a757b}
.err-tab.active{background:var(--orange)}

.rows{list-style:none}
.rows li{height:30px;display:flex;align-items:center;padding-left:15px;font-size:13px;color:#222}
.rows li:nth-child(odd){background:var(--grey-row)}
.axis-foot{font-family:"Titillium Web",sans-serif;font-weight:700;font-size:14px;color:var(--ink)}
</style>
</head>
<body>
<div class="stage">

  <!-- Sidebar -->
  <aside class="abs sidebar">
    <div class="abs brand">
      <div class="brand-name">Ledgerline <span class="brand-dot"></span></div>
      <div class="brand-tag">Performance Insight</div>
    </div>
    <div class="abs kpi-head">
      <div class="tick"><svg width="12" height="10" viewBox="0 0 12 10"><path d="M1 5l3.5 3.5L11 1" fill="none" stroke="#f7931e" stroke-width="2"/></svg></div>
      <h2>KPI's</h2>
      <div class="overall">Overall <b>YTD Accuracy 97.41%</b></div>
      <div class="caret"></div>
    </div>
    <ul class="abs kpi-list">
      <li>Claims Audited:<span class="lead"></span><b>4859</b></li>
      <li>Avg. Claims Audited per day:<span class="lead"></span><b>6.7</b></li>
      <li>Errors Found:<span class="lead"></span><b>2147</b></li>
      <li>Financial Impact:<span class="lead"></span><b>$1,462,139</b></li>
      <li>Total Claims Posted:<span class="lead"></span><b>17,773,591</b></li>
      <li>Total Encounter Claims:<span class="lead"></span><b>93,984,586</b></li>
      <li>Total Auto Adjudication Claim Count:<span class="lead"></span><b>920,918</b></li>
      <li>Total Adjustment Claim Count:<span class="lead"></span><b>920,918</b></li>
      <li>Total Denied Claim Count:<span class="lead"></span><b>133,523</b></li>
      <li>Total Dollars Paid:<span class="lead"></span><b>$5,669,835,044</b></li>
      <li>Auto Adjudication Rate:<span class="lead"></span><b>$0.052</b></li>
      <li>Adjustment Rate:<span class="lead"></span><b>1.345%</b></li>
    </ul>
    <div class="abs scroll-thumb"></div>

    <div class="abs ratios">
      <svg class="abs" style="left:0;top:0" width="391" height="344" viewBox="0 640 391 344">
        <path d="M158 735 A68 68 0 1 1 140 700" fill="none" stroke="#f7931e" stroke-width="3"/>
        <path d="M351 855 A68 68 0 1 1 336 836" fill="none" stroke="#f7931e" stroke-width="3" transform="rotate(-40 299 886)"/>
      </svg>
      <div class="abs ring-label" style="left:54px;top:82px;width:80px">Paid<br>vs<br>Denied</div>
      <div class="abs ring-label" style="left:259px;top:216px;width:80px">Paid<br>vs<br>Encounter</div>

      <div class="abs" style="left:192px;top:77px;display:flex;gap:14px">
        <div class="stat"><small>Paid</small><span>99.3%</span></div>
        <div class="stat-divider"></div>
        <div class="stat"><small>Denied</small><span>0.7%</span></div>
      </div>
      <div class="abs" style="left:34px;top:221px;display:flex;gap:14px">
        <div class="stat"><small>Paid</small><span>99.3%</span></div>
        <div class="stat-divider"></div>
        <div class="stat"><small>Denied</small><span>0.7%</span></div>
      </div>
    </div>
  </aside>

  <!-- Top navigation -->
  <nav class="abs topnav">
    <div class="tab active" style="width:205px">Accuracy Results</div>
    <div class="tab" style="width:196px">Processor Accuracy</div>
    <div class="tab" style="width:177px">Manage Users</div>
  </nav>
  <svg class="abs" style="left:1098px;top:28px" width="26" height="24" viewBox="0 0 26 24">
    <rect x="1" y="6" width="20" height="15" rx="1" fill="#3f86a1"/>
    <path d="M1 7l10 7 10-7" fill="none" stroke="#174d63" stroke-width="1.5"/>
    <circle cx="21" cy="5" r="5" fill="#f7931e"/>
    <text x="21" y="8" font-size="8" fill="#fff" text-anchor="middle" font-family="Open Sans">5</text>
  </svg>
  <div class="abs user" style="left:1146px">
    <div class="avatar" role="img" aria-label="User profile photo"></div>
    <span class="hi">Hi Mara</span>
  </div>
  <svg class="abs" style="left:1278px;top:34px" width="14" height="10"><path d="M0 1h13L6.5 9z" fill="#3f86a1"/></svg>
  <svg class="abs" style="left:1309px;top:28px" width="24" height="24" viewBox="0 0 24 24">
    <circle cx="12" cy="12" r="8" fill="none" stroke="#3f86a1" stroke-width="5" stroke-dasharray="3.2 3.1"/>
    <circle cx="12" cy="12" r="6" fill="#3f86a1"/><circle cx="12" cy="12" r="2.5" fill="#174d63"/>
  </svg>

  <!-- YTD panel -->
  <section class="abs panel" style="left:400px;top:90px;width:934px;height:360px">
    <svg class="abs" style="left:28px;top:18px" width="26" height="26" viewBox="0 0 26 26">
      <circle cx="13" cy="13" r="9" fill="none" stroke="#1d4f66" stroke-width="2"/>
      <circle cx="13" cy="13" r="4" fill="none" stroke="#1d4f66" stroke-width="2"/>
      <path d="M13 0v6M13 20v6M0 13h6M20 13h6" stroke="#1d4f66" stroke-width="2"/>
    </svg>
    <div class="abs panel-title" style="left:65px;top:17px">YTD overall accuracy Results</div>
    <div class="abs hint" style="left:312px;top:23px"><span style="color:#ccc;font-style:normal;margin-right:18px">|</span>Click the bars to view YTD details for the specific region</div>
    <div class="abs select" style="left:714px;top:15px;width:166px;height:32px">End to End <svg width="12" height="8"><path d="M0 0h12L6 8z" fill="#aab"/></svg></div>
    <div class="abs menu" style="left:897px;top:21px"><i></i><i></i><i></i></div>
  </section>
  <svg class="abs" style="left:400px;top:90px" width="934" height="360" viewBox="400 90 934 360" font-family="Open Sans">
    <defs>
      <linearGradient id="barFill" x1="0" y1="0" x2="0" y2="1">
        <stop offset="0" stop-color="#f9ad2a"/><stop offset="1" stop-color="#f5821f"/>
      </linearGradient>
    </defs>
    <rect x="418" y="150" width="48" height="240" fill="#f1f2f3"/>
    <rect x="400" y="390" width="934" height="60" fill="#ebecec"/>
    <g stroke="#e2e4e5" stroke-width="1">
      <line x1="418" y1="150" x2="1316" y2="150"/>
      <line x1="418" y1="193" x2="1316" y2="193"/>
      <line x1="418" y1="233" x2="1316" y2="233"/>
      <line x1="418" y1="272" x2="1316" y2="272"/>
      <line x1="418" y1="312" x2="1316" y2="312"/>
      <line x1="418" y1="351" x2="1316" y2="351"/>
      <line x1="418" y1="150" x2="418" y2="390"/>
      <line x1="1316" y1="150" x2="1316" y2="390"/>
      <line x1="626" y1="150" x2="626" y2="390"/>
      <line x1="794" y1="150" x2="794" y2="390"/>
      <line x1="966" y1="150" x2="966" y2="390"/>
      <line x1="1137" y1="150" x2="1137" y2="390"/>
    </g>
    <g fill="#d9dcde">
      <circle cx="626" cy="193" r="3"/><circle cx="626" cy="233" r="3"/><circle cx="626" cy="272" r="3"/><circle cx="626" cy="312" r="3"/><circle cx="626" cy="351" r="3"/>
      <circle cx="794" cy="193" r="3"/><circle cx="794" cy="233" r="3"/><circle cx="794" cy="272" r="3"/><circle cx="794" cy="312" r="3"/><circle cx="794" cy="351" r="3"/>
      <circle cx="966" cy="193" r="3"/><circle cx="966" cy="233" r="3"/><circle cx="966" cy="272" r="3"/><circle cx="966" cy="312" r="3"/><circle cx="966" cy="351" r="3"/>
      <circle cx="1137" cy="193" r="3"/><circle cx="1137" cy="233" r="3"/><circle cx="1137" cy="272" r="3"/><circle cx="1137" cy="312" r="3"/><circle cx="1137" cy="351" r="3"/>
    </g>
    <g font-size="12" fill="#555">
      <text x="431" y="178">100</text><text x="431" y="218">97.5</text><text x="431" y="257">95</text>
      <text x="431" y="297">92.5</text><text x="431" y="336">90</text><text x="431" y="376">87.5</text>
    </g>
    <g fill="url(#barFill)">
      <rect x="516" y="230" width="58" height="160"/>
      <rect x="680" y="219" width="58" height="171"/>
      <rect x="852" y="261" width="58" height="129"/>
      <rect x="1024" y="230" width="58" height="160"/>
      <rect x="1194" y="230" width="58" height="160"/>
    </g>
    <g font-size="12" font-weight="700" fill="#fff" text-anchor="middle">
      <text x="545" y="252">97.7%</text><text x="709" y="240">98.5%</text><text x="881" y="284">96.8%</text>
      <text x="1053" y="252">97.7%</text><text x="1223" y="252">94.9%</text>
    </g>
    <g font-size="13" font-weight="600" fill="#1d4f66" text-anchor="middle">
      <text x="543" y="426">Colorado</text><text x="709" y="426">Georgia</text><text x="882" y="426">Hawaii</text>
      <text x="1056" y="426">Midatlantic</text><text x="1223" y="426">Northwest</text>
    </g>
  </svg>

  <!-- Error impact -->
  <div class="abs impact-bar">
    <svg width="24" height="22" viewBox="0 0 24 22"><path d="M12 2L23 21H1z" fill="none" stroke="#fff" stroke-width="1.8"/><path d="M12 9v6M12 17v2" stroke="#fff" stroke-width="1.8"/></svg>
    <h3>Error impact for june 2016</h3>
  </div>
  <div class="abs impact-select">All Regions <svg width="12" height="8"><path d="M0 0h12L6 8z" fill="#3f89a3"/></svg></div>
  <div class="abs" style="left:400px;top:519px;width:934px;height:46px;background:var(--white)"></div>
  <div class="abs err-tabs">
    <div class="err-tab active" style="width:141px">All Errors</div>
    <div class="err-tab" style="width:144px">Providers</div>
    <div class="err-tab" style="width:154px">Employers</div>
    <div class="err-tab" style="width:163px">Line Of Business</div>
  </div>

  <section class="abs panel" style="left:400px;top:570px;width:934px;height:414px"></section>
  <div class="abs" style="left:800px;top:570px;width:1px;height:414px;background:#dcdfe0"></div>
  <div class="abs" style="left:400px;top:927px;width:934px;height:1px;background:#dcdfe0"></div>

  <div class="abs panel-title" style="left:418px;top:585px;font-size:16px">Top 10 Error Reasons</div>
  <div class="abs regions" style="left:602px;top:589px"><span style="color:#aaa;margin-right:14px">|</span>All Regions</div>
  <div class="abs panel-title" style="left:813px;top:585px;font-size:16px">Top 10 Error Reasons - Financial Impact</div>
  <div class="abs regions" style="left:1144px;top:590px"><span style="color:#aaa;margin-right:14px">|</span>All Regions</div>
  <div class="abs menu" style="left:1297px;top:589px"><i></i><i></i><i></i></div>

  <ul class="abs rows" style="left:400px;top:625px;width:195px">
    <li>Incorrect Contract ...</li><li>Claim Paid Incorrectly</li><li>Not A Halvern Benefit.&nbsp; Bill...</li>
    <li>Incorrect Co-Pay / C...</li><li>Copay Amount Not Correct</li><li>Did Not Follow Desk ...</li>
    <li>Did Not Follow Pnp</li><li>Claim Denied In Error...</li><li>Unknown</li><li>Denied Incorrectly -...</li>
  </ul>
  <ul class="abs rows" style="left:800px;top:625px;width:197px">
    <li>Incorrect Contract ...</li><li>Claim Paid Incorrectly</li><li>Not A Halvern Benefit.&nbsp; Bill...</li>
    <li>Incorrect Co-Pay / C...</li><li>Copay Amount Not Correct</li><li>Did Not Follow Desk ...</li>
    <li>Did Not Follow Pnp</li><li>Claim Denied In Error...</li><li>Unknown</li><li>Denied Incorrectly -...</li>
  </ul>

  <!-- Count chart -->
  <svg class="abs" style="left:595px;top:625px" width="205" height="359" viewBox="595 625 205 359" font-family="Open Sans">
    <g stroke="#eceeef"><line x1="635" y1="625" x2="635" y2="927"/><line x1="675" y1="625" x2="675" y2="927"/><line x1="715" y1="625" x2="715" y2="927"/><line x1="753" y1="625" x2="753" y2="927"/></g>
    <g fill="#f7931e">
      <rect x="595" y="637" width="140" height="5"/><rect x="595" y="667" width="104" height="5"/><rect x="595" y="697" width="100" height="5"/>
      <rect x="595" y="727" width="96" height="5"/><rect x="595" y="757" width="80" height="5"/><rect x="595" y="787" width="80" height="5"/>
      <rect x="595" y="814" width="72" height="5"/><rect x="595" y="846" width="60" height="5"/><rect x="595" y="875" width="60" height="5"/>
      <rect x="595" y="904" width="60" height="5"/>
    </g>
    <g fill="#d8353c">
      <circle cx="734" cy="640" r="9"/><circle cx="697" cy="671" r="9"/><circle cx="695" cy="700" r="9"/>
      <circle cx="691" cy="732" r="9"/><circle cx="675" cy="761" r="9"/><circle cx="675" cy="792" r="9"/>
      <circle cx="667" cy="818" r="9"/><circle cx="655" cy="848" r="9"/><circle cx="655" cy="877" r="9"/><circle cx="655" cy="906" r="9"/>
    </g>
    <g font-size="10" font-weight="700" fill="#fff" text-anchor="middle">
      <text x="734" y="644">35</text><text x="697" y="675">26</text><text x="695" y="704">24</text><text x="691" y="736">23</text>
      <text x="675" y="765">20</text><text x="675" y="796">20</text><text x="667" y="822">19</text><text x="655" y="852">14</text>
      <text x="655" y="881">14</text><text x="655" y="910">12</text>
    </g>
    <g fill="#fff" stroke="#c8ccce"><circle cx="595" cy="957" r="13"/><circle cx="635" cy="957" r="13"/><circle cx="675" cy="957" r="13"/><circle cx="715" cy="957" r="13"/><circle cx="753" cy="957" r="13"/></g>
    <g font-size="12" font-weight="600" fill="#333" text-anchor="middle">
      <text x="595" y="961">0</text><text x="635" y="961">10</text><text x="675" y="961">20</text><text x="715" y="961">30</text><text x="753" y="961">40</text>
    </g>
  </svg>
  <div class="abs axis-foot" style="left:466px;top:947px">COUNT</div>

  <!-- Amount chart -->
  <svg class="abs" style="left:997px;top:625px" width="337" height="359" viewBox="997 625 337 359" font-family="Open Sans">
    <g stroke="#eceeef"><line x1="1040" y1="625" x2="1040" y2="927"/><line x1="1090" y1="625" x2="1090" y2="927"/><line x1="1140" y1="625" x2="1140" y2="927"/><line x1="1190" y1="625" x2="1190" y2="927"/><line x1="1240" y1="625" x2="1240" y2="927"/><line x1="1290" y1="625" x2="1290" y2="927"/></g>
    <g fill="#f7931e">
      <rect x="1132" y="639" width="110" height="5"/><rect x="1176" y="669" width="66" height="5"/><rect x="1226" y="698" width="16" height="5"/>
      <rect x="1226" y="728" width="16" height="5"/><rect x="1226" y="758" width="16" height="5"/><rect x="1226" y="789" width="16" height="5"/>
      <rect x="1206" y="816" width="36" height="5"/><rect x="1226" y="847" width="16" height="5"/><rect x="1226" y="877" width="16" height="5"/>
      <rect x="1226" y="907" width="16" height="5"/>
    </g>
    <g fill="#d8353c">
      <rect x="1240" y="637" width="10" height="10"/><rect x="1240" y="667" width="10" height="10"/><rect x="1240" y="696" width="10" height="10"/>
      <rect x="1240" y="726" width="10" height="10"/><rect x="1240" y="756" width="10" height="10"/><rect x="1240" y="787" width="10" height="10"/>
      <rect x="1240" y="814" width="10" height="10"/><rect x="1240" y="845" width="10" height="10"/><rect x="1240" y="875" width="10" height="10"/>
      <rect x="1240" y="905" width="10" height="10"/>
    </g>
    <g fill="#8a9399">
      <polygon points="1061,632 1132,632 1132,652 1061,652 1053,642"/>
      <polygon points="1106,662 1176,662 1176,682 1106,682 1098,672"/>
      <polygon points="1155,691 1226,691 1226,711 1155,711 1147,701"/>
      <polygon points="1155,721 1226,721 1226,741 1155,741 1147,731"/>
      <polygon points="1155,751 1226,751 1226,771 1155,771 1147,761"/>
      <polygon points="1155,782 1226,782 1226,802 1155,802 1147,792"/>
      <polygon points="1136,809 1206,809 1206,829 1136,829 1128,819"/>
      <polygon points="1155,840 1226,840 1226,860 1155,860 1147,850"/>
      <polygon points="1155,870 1226,870 1226,890 1155,890 1147,880"/>
      <polygon points="1155,900 1226,900 1226,920 1155,920 1147,910"/>
      <polygon points="1250,632 1320,632 1328,642 1320,652 1250,652"/>
      <polygon points="1250,662 1320,662 1328,672 1320,682 1250,682"/>
      <polygon points="1250,691 1320,691 1328,701 1320,711 1250,711"/>
      <polygon points="1250,721 1320,721 1328,731 1320,741 1250,741"/>
      <polygon points="1250,751 1320,751 1328,761 1320,771 1250,771"/>
      <polygon points="1250,782 1320,782 1328,792 1320,802 1250,802"/>
      <polygon points="1250,809 1320,809 1328,819 1320,829 1250,829"/>
      <polygon points="1250,840 1320,840 1328,850 1320,860 1250,860"/>
      <polygon points="1250,870 1320,870 1328,880 1320,890 1250,890"/>
      <polygon points="1250,900 1320,900 1328,910 1320,920 1250,920"/>
    </g>
    <g font-size="12" font-weight="600" fill="#fff" text-anchor="middle">
      <text x="1094" y="647">$ -65155.67</text><text x="1140" y="677">$ -26915.92</text><text x="1192" y="706">$ -245</text>
      <text x="1188" y="736">$ 0</text><text x="1190" y="766">$ -295</text><text x="1188" y="797">$ 0</text>
      <text x="1170" y="824">$ -29341.33</text><text x="1188" y="855">$ 0</text><text x="1188" y="885">$ 0</text><text x="1188" y="915">$ 0</text>
      <text x="1289" y="647">$ 12510.63</text><text x="1289" y="677">$ 2919.39</text><text x="1289" y="706">$ 0</text>
      <text x="1289" y="736">$ 693.01</text><text x="1289" y="766">$ 10</text><text x="1289" y="797">$ 0</text>
      <text x="1289" y="824">$ 10390.26</text><text x="1289" y="855">$ 6509.7</text><text x="1289" y="885">$ 331.1</text><text x="1289" y="915">$ 1805.56</text>
    </g>
    <g font-size="13" font-weight="600" fill="#333" text-anchor="middle">
      <text x="1035" y="960">-80k</text><text x="1089" y="960">-60k</text><text x="1140" y="960">-40k</text>
      <text x="1191" y="960">-20k</text><text x="1239" y="960">0k</text><text x="1292" y="960">20k</text>
    </g>
  </svg>
  <div class="abs axis-foot" style="left:855px;top:947px">$ AMOUNT</div>

</div>
</body>
</html>
```